nine-parts.com

We are a small dollar lending company that will revolutionize the industry. We will do this by being completely transparent, fee free, etc and an interest rate that normal people can afford to pay. Over 10X less than our competition. We only allow our members to pay bills " bills paid fast", within 72 hours. Payday loans typically charge from 390%-600% with a terrible payback structure. We charge 36%, period, with a payback structure over 12 months. Our site will be very simple and easy to use but elegant at the same time. We do not want the site to be too busy, less is more and easier. We will have; Home, The Story, Why 9parts.com, Are you eligible? Members, Clients. To become a member you have to be referred by a current client of 9parts.com. A lot of the busy stuff will be saved for the Members and Clients sections. The feel must be elegant, easy to use and very simple to understand. I am looking for the green, white and black combinations of colors, very similar to my logo that was designed by Pixelmoor.

```html
<!DOCTYPE html>
<html lang="en">
<head>
<meta charset="utf-8">
<title>nine-parts.com</title>
<link rel="stylesheet" href="https://fonts.googleapis.com/css2?family=Lato:wght@300;400;700&family=League+Gothic&family=Ubuntu:wght@400&display=swap">
<style>
:root{
  --green:#8dc63f;
  --green-light:#a6d45e;
  --green-dark:#6fa52c;
  --button:#9bcd50;
  --button-edge:#6b9f2c;
  --ink:#222222;
  --text:#444444;
  --bar:#2b2b2b;
  --bar-active:#000000;
  --grey:#a9a9a9;
  --panel:#e9e9e9;
  --line:#dcdcdc;
  --white:#ffffff;
}
*{box-sizing:border-box;margin:0;padding:0}
html,body{width:1167px;height:1200px;overflow:hidden;background:var(--white);font-family:"Lato",sans-serif;color:var(--text)}
.page{position:relative;width:1167px;height:1200px}

.site-header{position:absolute;left:0;top:0;width:100%;height:105px}
.brand{position:absolute;left:168px;top:30px;display:flex;align-items:center;gap:10px;font-family:"Lato",sans-serif;font-weight:400;font-size:30px;color:var(--ink);letter-spacing:-.5px}
.brand-dot{width:34px;height:34px;border-radius:50%;background:var(--green)}
.social{position:absolute;left:882px;top:27px;display:flex;gap:5px}
.social span{width:26px;height:26px;background:var(--grey)}
.call{position:absolute;right:168px;top:62px;font-size:20px;font-weight:400;color:var(--ink)}
.call em{font-style:normal;font-weight:300;color:var(--green)}

.main-nav{position:absolute;left:0;top:105px;width:100%;height:44px;background:var(--bar)}
.main-nav ul{list-style:none;display:flex;position:absolute;left:167px;width:832px;height:44px}
.main-nav li{flex:1;display:flex;align-items:center;justify-content:center;font-size:11.5px;color:var(--white);text-transform:uppercase;border-right:1px solid #454545;letter-spacing:-.2px;white-space:nowrap}
.main-nav li.active{background:var(--bar-active)}

.hero{position:absolute;left:0;top:149px;width:100%;height:323px;overflow:hidden;background:linear-gradient(90deg,#86c23c 0%,#9dd253 25%,#8dc63f 55%,#8cc63e 100%)}
.hero-photo{position:absolute;left:230px;top:0;width:380px;height:323px;background:radial-gradient(ellipse at 55% 45%,#3c3f44 0%,#26282c 45%,rgba(38,40,44,0) 72%)}
.hero-copy{position:absolute;left:658px;top:40px;width:280px}
.hero-copy .rule{height:1px;background:rgba(255,255,255,.85)}
.hero-kicker{font-family:"League Gothic",sans-serif;font-weight:400;font-size:32px;line-height:34px;color:var(--ink);margin-top:2px;letter-spacing:0}
.hero-title{font-family:"League Gothic",sans-serif;font-weight:400;font-size:43px;line-height:42px;color:var(--white);letter-spacing:-.3px;white-space:nowrap;margin-bottom:4px}
.hero-list{list-style:none;margin-top:3px}
.hero-list li{display:flex;align-items:center;gap:8px;height:33.4px;font-family:"Ubuntu",sans-serif;font-size:20.5px;color:var(--ink);white-space:nowrap}
.hero-list svg{width:22px;height:20px;flex:none}

.feature{position:absolute;top:525px;width:240px;height:388px;background:var(--white);border:1px solid var(--line);box-shadow:0 1px 3px rgba(0,0,0,.08);text-align:center}
.feature-head{height:104px;background:var(--panel)}
.feature h2{padding-top:15px;font-weight:300;font-size:20px;color:var(--ink);letter-spacing:.2px}
.feature-icon{position:absolute;left:71px;top:52px;width:98px;height:98px;border-radius:50%;background:var(--green);display:flex;align-items:center;justify-content:center}
.feature p{margin:63px 10px 0;font-size:13px;line-height:20px;color:var(--text)}
.button{position:absolute;left:46px;top:311px;width:143px;height:51px;background:var(--button);border-bottom:4px solid var(--button-edge);border-radius:3px;font-size:13.5px;line-height:48px;color:#2f3b1f;text-transform:uppercase}

.clients{position:absolute;left:178px;top:962px;width:811px;height:110px;background:var(--panel);border:1px solid #cfcfcf;border-radius:4px}
.clients h3{position:absolute;left:12px;top:9px;font-weight:300;font-size:17px;color:var(--ink)}
.client-row{position:absolute;left:8px;top:40px;width:795px;height:50px;display:flex;justify-content:space-between;align-items:center}
.client-row span{font-size:15px;font-weight:700;color:#5a5a5a;text-transform:uppercase;letter-spacing:.3px}

.site-footer{position:absolute;left:0;top:1123px;width:100%;height:77px;background:var(--bar);text-align:center}
.footer-links{margin-top:18px;font-size:12px;color:var(--white);text-transform:uppercase;word-spacing:1px}
.footer-links i{font-style:normal;color:#999;margin:0 4px}
.copyright{margin-top:7px;font-size:12px;color:#cfcfcf}
</style>
</head>
<body>
<div class="page">
  <header class="site-header">
    <div class="brand"><span class="brand-dot"></span>nine-parts</div>
    <div class="social" aria-label="Social links"><span></span><span></span><span></span><span></span></div>
    <div class="call"><em>CALL US</em> 555.010.2040</div>
  </header>

  <nav class="main-nav">
    <ul>
      <li class="active">Home</li>
      <li>The Story</li>
      <li>Why 9parts.com</li>
      <li>Are You Eligible?</li>
      <li>Members</li>
      <li>Clients</li>
      <li>Contact Us</li>
    </ul>
  </nav>

  <section class="hero">
    <div class="hero-photo" role="img" aria-label="Photo of a businessman in a dark suit holding out a small glass globe"></div>
    <div class="hero-copy">
      <div class="rule"></div>
      <div class="hero-kicker">We are a</div>
      <div class="hero-title">DOLLAR LENDING COMPANY</div>
      <div class="rule"></div>
      <ul class="hero-list">
        <li><svg viewBox="0 0 22 20"><path d="M2 11l6 6L20 3" fill="none" stroke="#fff" stroke-width="3"/></svg>Completely Transparent</li>
        <li><svg viewBox="0 0 22 20"><path d="M2 11l6 6L20 3" fill="none" stroke="#fff" stroke-width="3"/></svg>Fee Free Service</li>
        <li><svg viewBox="0 0 22 20"><path d="M2 11l6 6L20 3" fill="none" stroke="#fff" stroke-width="3"/></svg>Affordable Interest Rate</li>
        <li><svg viewBox="0 0 22 20"><path d="M2 11l6 6L20 3" fill="none" stroke="#fff" stroke-width="3"/></svg>Pay Bills within 72 hours &amp;</li>
        <li><svg viewBox="0 0 22 20"><path d="M2 11l6 6L20 3" fill="none" stroke="#fff" stroke-width="3"/></svg>Much more</li>
      </ul>
    </div>
  </section>

  <article class="feature" style="left:181px">
    <div class="feature-head"><h2>THE STORY</h2></div>
    <div class="feature-icon">
      <svg width="46" height="42" viewBox="0 0 46 42"><path d="M12 3h28l-8 32H4z" fill="#fff"/><path d="M16 10h18M14 16h18" stroke="#8dc63f" stroke-width="3"/><path d="M4 35h28l2 4H6z" fill="#fff"/></svg>
    </div>
    <p>Small dollar loans are either too hard to get, take too long to process or just impossible to pay back. There are between 15mm-18mm people each year that require the use of small dollar loans, so you are not alone....</p>
    <div class="button">Know More</div>
  </article>

  <article class="feature" style="left:465px">
    <div class="feature-head"><h2>MEMBERS</h2></div>
    <div class="feature-icon">
      <svg width="56" height="40" viewBox="0 0 56 40"><circle cx="20" cy="11" r="10" fill="#fff"/><circle cx="39" cy="15" r="8" fill="#fff"/><path d="M2 40c0-12 8-17 18-17s18 5 18 17z" fill="#fff"/><path d="M30 40c0-9 4-14 10-14s14 4 14 14z" fill="#fff"/></svg>
    </div>
    <p>Lorem ipsum dolor sit amet, consectetur adipiscing elit. Sed quis nisi euismod, fermentum tellus a, lobortis quam. Vestibulum condimentum mi vitae diam tristique, egestas dignissim diam matti&nbsp; semper ut tortor.....</p>
    <div class="button">Know More</div>
  </article>

  <article class="feature" style="left:750px">
    <div class="feature-head"><h2>ARE YOU ELIGIBLE?</h2></div>
    <div class="feature-icon">
      <svg width="44" height="40" viewBox="0 0 44 40"><path d="M4 8h24v6H10v18h18v-8h6v14H4z" fill="#fff"/><path d="M12 17l7 7L38 4" fill="none" stroke="#fff" stroke-width="5"/></svg>
    </div>
    <p>Donec eleifend accumsan nisl, nec laoreet leo iaculis sit amet. Vivamus varius arcu eu sagittis aliquam. Vivamus accumsan cursus hendrerit. Vivamus eu magna rhoncus, consectetur metus ac, varius lacus. Donec ultricies, torto....</p>
    <div class="button">Know More</div>
  </article>

  <section class="clients">
    <h3>Our Clients</h3>
    <div class="client-row">
      <span>Brisa</span>
      <span>Kestrel</span>
      <span>Plumcrest</span>
      <span>Wavelark</span>
      <span>Ironvale</span>
      <span>Harvest Table</span>
      <span>Poppington</span>
    </div>
  </section>

  <footer class="site-footer">
    <div class="footer-links">Home<i>/</i>The Story<i>/</i>Why 9parts.com<i>/</i>Are You Eligible?<i>/</i>Members<i>/</i>Clients<i>/</i>Contact Us</div>
    <div class="copyright">Copyright © 2014 nine-parts.com. All rights reserved.</div>
  </footer>
</div>
</body>
</html>
```